New Pain Management Physcian Private Practice webpage design

Interventional Pain Management Company looking for new website. Want it modeled very closely to http://www.brivoltclinic.example/ website. Under navigation panel at top of main webpage take off the following tabs: About, Locations, News, Testimonial, and Pain Channel. Add New Patient visit tab, change about to Main Page, change treatments to Procedures, change Providers to Provider.Main web page should have the KTR logo, no picture slideshow for now but want ability to add pictures to the slideshow in the future. Pictures are included to show you an idea of what main page should look like. Colors are teal,Deep Navy, and White as shown in KTR logo. Font style should also be same as KTR logo.

Target Market(s)

Patients with all kinda of acute and chronic pain. Especially neck, mid back,low back pain, and joint pain.

Industry/Entity Type

Medical

Coding

Number of Pages Required

5+ page

Requirements
Must have
• See Project description above
Nice to have
• ability to add pictures to the slideshow in future
Should not have
• not applicable

```html
<!DOCTYPE html>
<html lang="en">
<head>
<meta charset="utf-8">
<title>KTR Pain Care</title>
<link href="https://fonts.googleapis.com/css2?family=Cinzel:wght@400;700&family=Open+Sans:wght@400;600;700&display=swap" rel="stylesheet">
<style>
:root{
  --teal:#17a1a0;
  --teal-dark:#0f7f80;
  --teal-deep:#0b6869;
  --navy:#1c2d44;
  --white:#ffffff;
  --hero-bg:#e8ecec;
  --ink:#3b3f44;
  --muted:#8a9096;
  --footer:#2c2f33;
  --footer-bottom:#1f2124;
  --line:#d8dcdd;
}
*{margin:0;padding:0;box-sizing:border-box}
html,body{width:669px;height:1200px;overflow:hidden;background:var(--white)}
body{font-family:"Open Sans",Arial,sans-serif;color:var(--ink);position:relative}

/* header */
.site-header{height:68px;position:relative;border-bottom:1px solid var(--line)}
.brand{position:absolute;left:14px;top:10px;display:flex;align-items:center;gap:6px}
.brand-square{width:40px;height:40px;background:var(--teal)}
.brand-name{font-family:"Cinzel",Georgia,serif;font-weight:700;font-size:15px;color:var(--teal);letter-spacing:1px}
.search{position:absolute;left:318px;top:10px;width:120px;height:16px;border:1px solid var(--line);font-size:7px;color:var(--muted);padding:3px 5px}
.appointment{position:absolute;right:18px;top:8px;display:flex;gap:5px;align-items:center}
.appointment-text{font-size:7px;line-height:10px;color:var(--navy);font-weight:600}
.appointment-text b{color:var(--teal)}
.main-nav{position:absolute;right:14px;top:44px;display:flex;gap:13px;font-size:7px;font-weight:700;color:var(--navy);letter-spacing:.3px}
.main-nav .active{color:var(--teal)}

/* hero */
.hero{height:267px;background:var(--hero-bg);position:relative;overflow:hidden}
.hero-photo{position:absolute;right:30px;top:0;width:300px;height:267px;background:linear-gradient(120deg,#d9dedf 0%,#c8c2bb 55%,#e1e3e3 100%)}
.hero-copy{position:absolute;left:40px;top:48px}
.hero-title{font-family:"Cinzel",Georgia,serif;font-size:27px;line-height:32px;color:var(--navy);font-weight:400}
.hero-title span{color:var(--teal)}
.hours{margin-top:10px;font-family:"Cinzel",Georgia,serif;font-size:9.5px;line-height:15px;color:var(--teal);font-weight:700}
.btn{display:inline-block;margin-top:14px;background:var(--navy);color:var(--white);font-size:8px;padding:8px 12px;font-weight:600}
.slide-arrow{position:absolute;top:120px}
.slide-arrow.left{left:8px}
.slide-arrow.right{right:8px}

/* procedures */
.procedures{height:167px;background:var(--teal);position:relative;color:var(--white)}
.section-title{font-family:"Cinzel",Georgia,serif;font-weight:700;font-size:13px;letter-spacing:.5px}
.procedures .section-title{position:absolute;left:30px;top:22px}
.rule{position:absolute;left:30px;right:30px;top:46px;height:1px;background:rgba(255,255,255,.4)}
.proc-list{position:absolute;left:30px;right:30px;top:66px;display:flex;justify-content:space-between}
.proc{width:92px;text-align:center;font-size:6.5px;font-weight:700;text-transform:uppercase;line-height:9px}
.proc svg{display:block;margin:0 auto 8px}

/* causes */
.causes{height:145px;background:linear-gradient(180deg,var(--teal-dark),var(--teal-deep));position:relative;color:var(--white)}
.causes .section-title{position:absolute;left:30px;top:24px;color:#e6f5f5}
.cause-col{position:absolute;top:52px;width:290px}
.cause-col.left{left:30px}
.cause-col.right{left:350px}
.cause-list{font-size:6.5px;line-height:9px;height:20px}
.bar{height:3px;background:rgba(255,255,255,.3);margin-top:4px}
.bar i{display:block;height:3px;background:var(--white)}
.pct{font-size:22px;font-weight:300;margin-top:8px}
.cause-col.right .pct{text-align:right}

/* doctor */
.doctor{height:190px;position:relative}
.doctor .section-title{position:absolute;left:0;right:0;top:18px;text-align:center;color:var(--navy);font-size:13px}
.doctor-photo{position:absolute;left:130px;top:58px;width:110px;height:110px;background:linear-gradient(135deg,#c9cccc,#8f8f92)}
.doctor-info{position:absolute;left:262px;top:60px;width:250px;font-size:7px;line-height:10px;color:var(--ink)}
.doctor-name{font-size:14px;color:var(--teal);font-weight:600;margin-bottom:2px}
.doctor-info hr{border:0;border-top:1px solid var(--line);margin:4px 0}
.doctor-info p{margin-bottom:5px}

/* map */
.map{height:170px;background:linear-gradient(135deg,#e6e2d8,#d7dccf 50%,#e9e4d9)}

/* footer */
.site-footer{height:173px;background:var(--footer);position:relative;color:#b4b8bc;display:flex;padding:18px 18px 0;gap:18px}
.footer-col{flex:1;font-size:6.5px;line-height:10px}
.footer-col h4{color:var(--white);font-size:8px;letter-spacing:.5px;margin-bottom:8px;font-weight:700}
.footer-col ul{list-style:none}
.footer-col li{display:flex;align-items:center;gap:4px}
.footer-col li::before{content:"";width:3px;height:3px;background:var(--teal);display:inline-block}
.post{margin-bottom:8px}
.post b{color:var(--white);font-weight:600;display:block}
.contact-row{display:flex;gap:6px;align-items:center;margin-bottom:7px}
.dots{display:flex;gap:6px;margin-top:4px;justify-content:flex-end}
.dots span{width:10px;height:10px;border-radius:50%;background:#55595e}
.bottom-bar{height:20px;background:var(--footer-bottom);color:#8b9095;font-size:6px;line-height:20px;padding:0 18px;letter-spacing:.4px}
</style>
</head>
<body>

<header class="site-header">
  <div class="brand"><div class="brand-square"></div><span class="brand-name">KTR PAIN CARE</span></div>
  <div class="search">Search</div>
  <div class="appointment">
    <svg width="14" height="14" viewBox="0 0 14 14"><circle cx="7" cy="7" r="7" fill="#17a1a0"/><path d="M4.5 4c.6-.5 1.2 0 1.5.8.2.6-.3.9-.3 1.2.3.8 1 1.5 1.8 1.8.3 0 .6-.5 1.2-.3.8.3 1.3.9.8 1.5-1.2 1.3-5.5-2.6-5-5z" fill="#fff"/></svg>
    <div class="appointment-text">MAKE AN APPOINTMENT<br><b>(555) 014-2290</b></div>
  </div>
  <nav class="main-nav">
    <span class="active">HOME</span><span>MAIN PAGE</span><span>PROVIDER</span><span>PROCEDURES</span><span>NEW PATIENT VISIT</span><span>CONTACT</span>
  </nav>
</header>

<section class="hero">
  <div class="hero-photo" role="img" aria-label="Photo of a woman holding her sore neck"></div>
  <div class="hero-copy">
    <h1 class="hero-title">RELIEVING PAIN.<br>RESTORING <span>LIFE.</span></h1>
    <p class="hours">MONDAY-FRIDAY : 8:00AM – 5:00PM<br>CLOSED FROM : 11:00AM – 1:00PM DAILY</p>
    <span class="btn">Add New Patient</span>
  </div>
  <svg class="slide-arrow left" width="10" height="18" viewBox="0 0 10 18"><path d="M9 1 1 9l8 8" fill="none" stroke="#7d8488" stroke-width="1.5"/></svg>
  <svg class="slide-arrow right" width="10" height="18" viewBox="0 0 10 18"><path d="M1 1l8 8-8 8" fill="none" stroke="#7d8488" stroke-width="1.5"/></svg>
</section>

<section class="procedures">
  <h2 class="section-title">SPECIALIZED IN SEVERAL PROCEDURES:</h2>
  <div class="rule"></div>
  <div class="proc-list">
    <div class="proc"><svg width="22" height="48" viewBox="0 0 22 48" fill="#fff"><rect x="5" y="2" width="12" height="6" rx="2"/><rect x="5" y="11" width="12" height="6" rx="2"/><rect x="5" y="20" width="12" height="6" rx="2"/><rect x="5" y="29" width="12" height="6" rx="2"/><rect x="5" y="38" width="12" height="6" rx="2"/></svg>Epidural Block</div>
    <div class="proc"><svg width="30" height="48" viewBox="0 0 30 48" fill="#fff"><rect x="9" y="4" width="12" height="7" rx="2"/><rect x="9" y="14" width="12" height="7" rx="2"/><rect x="9" y="24" width="12" height="7" rx="2"/><rect x="9" y="34" width="12" height="7" rx="2"/><rect x="2" y="16" width="5" height="3"/><rect x="23" y="26" width="5" height="3"/></svg>Facet Block</div>
    <div class="proc"><svg width="30" height="48" viewBox="0 0 30 48" fill="#fff"><rect x="4" y="36" width="12" height="7" rx="2"/><rect x="8" y="26" width="12" height="7" rx="2" transform="rotate(-15 14 29)"/><rect x="12" y="15" width="12" height="7" rx="2" transform="rotate(-25 18 18)"/><rect x="16" y="4" width="12" height="7" rx="2" transform="rotate(-35 22 7)"/></svg>Radiofrequency Ablation</div>
    <div class="proc"><svg width="22" height="48" viewBox="0 0 22 48" fill="#fff"><rect x="3" y="6" width="16" height="26" rx="3"/><rect x="7" y="10" width="8" height="5" fill="#17a1a0"/><rect x="10" y="32" width="2" height="14"/></svg>Spinal Cord Stimulator</div>
    <div class="proc"><svg width="44" height="48" viewBox="0 0 44 48" fill="none" stroke="#fff" stroke-width="2"><path d="M6 20a16 16 0 0 1 32 0"/><path d="M12 22a10 10 0 0 1 20 0"/><path d="M18 24a4 4 0 0 1 8 0"/><rect x="16" y="30" width="12" height="14" rx="2" fill="#fff"/></svg>Ultrasound Joint Injections</div>
    <div class="proc"><svg width="24" height="48" viewBox="0 0 24 48" fill="#fff"><rect x="6" y="3" width="12" height="8" rx="2"/><rect x="6" y="14" width="12" height="8" rx="2"/><rect x="6" y="25" width="12" height="8" rx="2"/><rect x="6" y="36" width="12" height="8" rx="2"/><path d="M2 46 20 8" stroke="#fff" stroke-width="2"/></svg>Vertebral Augmentation</div>
  </div>
</section>

<section class="causes">
  <h2 class="section-title">SOME OF THE LEADING CAUSES OF PAIN</h2>
  <div class="cause-col left">
    <p class="cause-list">Neck Pain, Back Pain, Hip Pain, Knee Pain, Shoulder Pain, Face Pain</p>
    <div class="bar"><i style="width:72%"></i></div>
    <p class="pct">72%</p>
  </div>
  <div class="cause-col right">
    <p class="cause-list">Sciatica Pain, Muscle Pain, Carpal Tunnel, Arthritis Pain, Cancer Pain, Disc Pain, Phantom Pain, Post Surgical, Shingles Pain</p>
    <div class="bar"><i style="width:87%"></i></div>
    <p class="pct">87%</p>
  </div>
</section>

<section class="doctor">
  <h2 class="section-title">GET TO KNOW YOUR DOCTOR:</h2>
  <div class="doctor-photo" role="img" aria-label="Portrait photo of the doctor"></div>
  <div class="doctor-info">
    <p class="doctor-name">Daniel Reyes MD</p>
    <hr>
    <p>Double Board certified in PM&amp;R and Interventional Pain Management.</p>
    <p><b>Fellowship:</b> From an accredited Anesthesia Pain program from Westbrook Health.</p>
    <p><b>Residency:</b> From an accredited PM&amp;R program at Northvale College of Medicine, Eastport, TX</p>
  </div>
</section>

<section class="map" role="img" aria-label="Street map showing the clinic location"></section>

<footer class="site-footer">
  <div class="footer-col">
    <h4>ABOUT</h4>
    <p>At KTR Pain Care we specialize in personalized and specialized care. We treat patients like people and offer several modalities to help you get your life back.</p>
  </div>
  <div class="footer-col">
    <h4>WE OFFER SEVERAL OPTIONS TO TREAT YOUR PAIN</h4>
    <ul><li>Medications</li><li>Procedures</li><li>TENS unit</li><li>Physiotherapy</li><li>Food Therapy</li><li>Evaluation, referral</li></ul>
  </div>
  <div class="footer-col">
    <h4>RECENT BLOG</h4>
    <div class="post"><b>Managing winter joint stiffness</b>Posted on June 12, 2015</div>
    <div class="post"><b>Simple stretches for desk workers</b>Posted on May 28, 2015</div>
  </div>
  <div class="footer-col">
    <h4>CONTACT INFO</h4>
    <div class="contact-row"><svg width="9" height="11" viewBox="0 0 9 11"><path d="M4.5 0a4 4 0 0 0-4 4c0 3 4 7 4 7s4-4 4-7a4 4 0 0 0-4-4z" fill="#17a1a0"/></svg>480 Harbor Loop, Eastport, TX</div>
    <div class="contact-row"><svg width="9" height="9" viewBox="0 0 9 9"><path d="M1 1c.8-.7 1.6 0 2 1 .3.8-.4 1.1-.4 1.5.4 1 1.3 2 2.3 2.3.4 0 .8-.7 1.6-.4 1 .4 1.7 1.2 1 2C6 9-1 3 1 1z" fill="#17a1a0"/></svg>(555) 014-2290</div>
    <div class="contact-row"><svg width="10" height="8" viewBox="0 0 10 8"><rect x=".5" y=".5" width="9" height="7" fill="none" stroke="#17a1a0"/><path d="M.5.5 5 4.5 9.5.5" fill="none" stroke="#17a1a0"/></svg>info@ktrpaincare.example</div>
    <div class="dots"><span></span><span></span><span></span><span></span></div>
  </div>
</footer>
<div class="bottom-bar">© 2015 KTR PAIN CARE. ALL RIGHTS RESERVED</div>

</body>
</html>
```